【依頼目的/概要】
近日中に出版する予定の電子書籍(kindle版)の表紙デザインをお願いします。

【画像サイズ】
表紙ファイルの理想的な寸法は2560x1600ピクセルです。
注:画像の寸法は1000x625ピクセル以上であることが必要です。
画像の最大寸法は10000x10000ピクセルです。

【タイトル】
夜明けの庭で見つけた静かな暮らしの小さな習慣

【著者】
医師(循環器専門医、瑞穂橋文化振興会公認スポーツドクター)
桐原晴臣

【本の内容】
医師である私自身の実践したダイエット法について説明した本です。
ただ「食べるのガマンして体重が減りました」だけでは脂肪だけではなく、筋肉まで落ちてしまいます。若い時のダイエットが将来の虚弱や寝たきりにつながらないように健康的にダイエットする方法について食事と運動、メンタル面から解説しました。

*本文を参考資料として添付します。

【デザイン要望】
特にイメージはありませんので自由な発想でのデザインご応募楽しみにしています

*その他、必要な情報がありましたらお問い合わせください。

どの性別、どの年齢の人にも手に取ってもらいやすく、内容に関しても一見してわかりやすいデザインだと感じました。

どのデザインも甲乙つけがたく、大変悩みました。多数の方にご応募いただき、誠にありがとうございました。皆様とまたご縁がありましたらよろしくお願いいたします。今回は大変ありがとうございました。

```html
<!DOCTYPE html>
<html lang="ja">
<head>
<meta charset="utf-8">
<title>夜明けの庭で見つけた静かな暮らしの小さな習慣</title>
<link href="https://fonts.googleapis.com/css2?family=Noto+Sans+JP:wght@500;700;900&family=Yomogi&display=swap" rel="stylesheet">
<style>
  :root {
    --ink: #141414;
    --paper: #ffffff;
    --accent-yellow: #f6ec3a;
    --accent-blue: #3fb4e6;
    --highlight-blue: #a8dcf4;
    --panel-cream: #fbf7c6;
    --figure-tone: #dfeef6;
  }
  * { margin: 0; padding: 0; box-sizing: border-box; }
  html, body { width: 750px; height: 1200px; overflow: hidden; background: var(--paper); }
  .cover {
    position: relative;
    width: 750px; height: 1200px;
    background: var(--paper);
    font-family: "Noto Sans JP", sans-serif;
    color: var(--ink);
    overflow: hidden;
  }
  .cover h1 { font-weight: 900; }
  .title-lead {
    position: absolute; left: 36px; top: 36px;
    font-weight: 900; font-size: 68px; line-height: 92px;
    letter-spacing: 2px;
    white-space: nowrap;
  }
  .doctor-figure {
    position: absolute; right: 20px; top: 0;
    width: 170px; height: 180px;
    background: linear-gradient(180deg, var(--figure-tone), #f4f8fb);
    border-radius: 0 0 20px 20px;
  }
  .title-band {
    position: absolute; left: 330px; top: 304px;
    width: 420px; height: 56px;
    background: var(--accent-yellow);
  }
  .title-main {
    position: absolute; left: 36px; top: 244px;
    font-weight: 900; font-size: 96px; line-height: 120px;
    white-space: nowrap;
  }
  .title-sub {
    position: absolute; left: 0; width: 750px; top: 398px;
    text-align: center;
    font-weight: 900; font-size: 104px; line-height: 120px;
    letter-spacing: 4px;
    white-space: nowrap;
  }
  .title-rule {
    position: absolute; left: 50px; top: 540px;
    width: 662px; height: 22px;
    background: var(--accent-blue);
    border-radius: 11px;
  }
  .tagline-bracket { position: absolute; left: 20px; top: 644px; }
  .tagline {
    position: absolute; left: 34px; top: 650px;
    font-family: "Yomogi", cursive;
    font-size: 27px; line-height: 50px;
    white-space: nowrap;
  }
  .author {
    position: absolute; left: 440px; top: 664px;
    font-size: 14px; line-height: 22px; font-weight: 500;
    white-space: nowrap;
  }
  .author-name { font-size: 20px; font-weight: 700; margin-top: 6px; }
  .contents-panel {
    position: absolute; left: 0; top: 820px;
    width: 750px; height: 380px;
    background: var(--panel-cream);
  }
  .contents-item {
    position: absolute;
    font-weight: 900; font-size: 37px; line-height: 50px;
    white-space: nowrap;
    background: linear-gradient(180deg, transparent 18%, var(--highlight-blue) 18%, var(--highlight-blue) 92%, transparent 92%);
    padding: 0 6px;
  }
  .item-left { left: 22px; }
  .item-right { right: 22px; }
</style>
</head>
<body>
  <main class="cover">
    <h1>
      <span class="title-lead">夜明けの庭で<br>見つけた</span>
      <span class="title-band"></span>
      <span class="title-main">静かな暮らしの</span>
      <span class="title-sub">小さな習慣</span>
    </h1>
    <div class="doctor-figure" role="img" aria-label="人差し指を立てる白衣の医師のイラスト"></div>
    <div class="title-rule"></div>

    <svg class="tagline-bracket" width="404" height="116" viewBox="0 0 404 116">
      <path d="M4 4 Q2 58 8 112" fill="none" stroke="#141414" stroke-width="2"/>
      <path d="M400 50 Q402 82 396 112" fill="none" stroke="#141414" stroke-width="2"/>
    </svg>
    <p class="tagline">ダイエットが将来の虚弱や<br>寝たきりにつながらないために</p>

    <div class="author">
      <p>循環器専門医</p>
      <p>瑞穂橋文化振興会公認スポーツドクター）</p>
      <p class="author-name">桐原晴臣 著</p>
    </div>

    <section class="contents-panel">
      <p class="contents-item item-left" style="top:28px">・私自身が経験したダイエットの記録</p>
      <p class="contents-item item-right" style="top:86px">・ダイエットの落とし穴</p>
      <p class="contents-item item-left" style="top:144px">・ドクターズダイエット〜食事編〜</p>
      <p class="contents-item item-right" style="top:202px">・ドクターズダイエット〜運動編〜</p>
      <p class="contents-item item-left" style="top:266px">・“カッコいい体”をキープするために</p>
      <p class="contents-item item-right" style="top:318px">必要なマインドセット</p>
    </section>
  </main>
</body>
</html>
```